Tumble Tail (Pet Supplies) Home Page

For our Tumble Tail website, we want this to be fun and playful but with a touch of your creativity! Tumble Tail is a fun-loving brand that sells pet supplies and accessories focused on accentuating the love between pets and their owners. We want to advertise these products in a welcoming way, making the customer receive the happiness the brand offers.

Target Market(s)

Main demo: Female pet owners online shopping 18-34. Secondary demo: All pet owners online shopping 18-34.

Number of Pages Required

1 page

```html
<!DOCTYPE html>
<html lang="en">
<head>
<meta charset="utf-8">
<title>Tumble Tail – Pet Supplies and Accessories</title>
<link rel="stylesheet" href="https://fonts.googleapis.com/css2?family=Chewy&family=Lato:ital,wght@0,400;0,700;0,900;1,700&display=block">
<style>
:root{
  --teal:#2bb1ae;
  --teal-soft:#5cbfb9;
  --orange:#e8743d;
  --orange-soft:#f0a17b;
  --grey-pill:#b9b9b9;
  --page:#f2f7f7;
  --ink:#1f1f1f;
  --muted:#555;
  --card-line:#e1e6e6;
  --white:#fff;
  --font-display:"Chewy","Comic Sans MS","Chalkboard SE","Comic Neue",sans-serif;
  --font-text:"Lato","Helvetica Neue",Arial,sans-serif;
}
*{box-sizing:border-box;margin:0;padding:0}
html,body{width:1200px;height:4051px;overflow:hidden}
body{background:var(--page);font-family:var(--font-text);color:var(--ink)}
.page{position:relative;width:1200px;height:4051px;overflow:hidden;background:var(--page)}
.abs{position:absolute}
.display{font-family:var(--font-display);font-weight:400;letter-spacing:.5px}

/* hero */
.hero-photo{left:0;top:0;width:1200px;height:740px;
  background:linear-gradient(100deg,#3f5a24 0%,#6f8a3a 30%,#a88a52 55%,#c9a47a 70%,#5e7a34 100%)}
.brand{left:130px;top:122px;width:200px;text-align:center;color:var(--white);font-size:34px;line-height:1}
.brand-dot{left:205px;top:28px;width:50px;height:50px;border-radius:50%;background:var(--white)}
.nav{left:410px;top:57px;display:flex;gap:9px}
.nav a{display:block;height:35px;line-height:35px;padding:0 17px;border-radius:8px;color:var(--white);text-decoration:none;font-family:var(--font-display);font-weight:400;font-size:16px}
.nav .home,.nav .shop{background:var(--teal-soft)}
.nav .story{background:var(--orange)}
.nav .blog{background:var(--orange-soft)}
.nav .history{background:var(--grey-pill)}
.nav-icons{left:965px;top:60px;display:flex;gap:20px}
.cart-count{left:1040px;top:62px;width:14px;height:14px;border-radius:50%;background:var(--teal);color:#fff;font-size:9px;text-align:center;line-height:14px}
.hero-blob{left:140px;top:215px}
.hero-title{left:160px;top:285px;width:320px;text-align:center;color:var(--white);font-size:44px;line-height:47px}
.btn-shop{left:240px;top:446px;width:160px;height:46px;background:var(--orange);border-radius:4px;color:#fff;font-size:17px;text-align:center;line-height:46px}
.arrow{width:40px;height:40px;border:2px solid rgba(255,255,255,.7);border-radius:50%}

/* promo */
.promo{left:0;top:690px}
.promo-title{left:570px;top:828px;width:305px;text-align:center;color:var(--white);font-size:40px;line-height:43px}

/* section heads */
.sec-mark{width:32px;height:32px;border:4px solid var(--teal);border-radius:50%}
.sec-title{width:1200px;left:0;text-align:center;font-size:44px;color:var(--ink)}

/* products */
.card{width:231px;height:376px;background:var(--white);border:2px solid var(--card-line);border-radius:30px;overflow:hidden}
.card .shot{position:absolute;left:30px;top:28px;width:170px;height:210px;border-radius:14px}
.card .cart{position:absolute;right:18px;top:22px;width:34px;height:34px;border-radius:50%;background:var(--orange);display:flex;align-items:center;justify-content:center}
.card .name{position:absolute;left:0;top:256px;width:100%;text-align:center;font-weight:700;font-size:16px}
.card .desc{position:absolute;left:0;top:280px;width:100%;text-align:center;font-size:16px;color:var(--muted)}
.card .rule{position:absolute;left:0;top:318px;width:100%;border-top:2px solid var(--card-line)}
.card .price{position:absolute;left:0;top:334px;width:100%;text-align:center;font-weight:700;font-style:italic;font-size:17px;color:var(--teal)}

/* pay later */
.paylater{left:0;top:2290px}
.pay-title{left:0;top:2440px;width:1200px;text-align:center;color:var(--white);font-size:46px}
.pay-btn{top:2540px;width:257px;height:98px;background:var(--white);border-radius:34px;display:flex;align-items:center;justify-content:center;font-size:38px;font-weight:700;color:var(--ink)}

/* testimonials */
.quote{width:446px;height:250px;background:var(--white);border-radius:34px}
.quote .avatar{position:absolute;left:26px;top:50px;width:140px;height:140px;border-radius:50%}
.quote .who{position:absolute;left:193px;top:36px;font-weight:900;font-size:17px}
.quote .words{position:absolute;left:193px;top:70px;width:228px;font-size:15px;line-height:24px;color:#222}

/* footer */
.footer{left:0;top:3615px;width:1200px;height:436px;background:var(--teal)}
.rewards{left:144px;top:3590px;width:132px;height:42px;border-radius:21px;background:#3a3f9b;border:2px solid #fff;color:#fff;font-size:11px;font-weight:900;letter-spacing:.5px;display:flex;align-items:center;justify-content:center;gap:7px}
.chat{left:1082px;top:3585px;width:53px;height:53px;border-radius:50%;background:#6f8ecf;border:3px solid #fff;display:flex;align-items:center;justify-content:center}
.foot-brand{left:130px;top:3790px;width:200px;text-align:center;color:#fff;font-size:36px}
.foot-dot{left:195px;top:3700px;width:70px;height:70px;border-radius:50%;border:7px solid #fff}
.foot-col h4{color:#fff;font-size:17px;font-weight:900;letter-spacing:.5px;margin-bottom:16px}
.foot-col li{list-style:none;color:#e3f6f5;font-size:15px;line-height:27px}
.contact-row{display:flex;gap:16px;align-items:flex-start;color:#fff;font-size:15px;font-weight:700;line-height:19px;margin-bottom:24px}
.social{display:flex;gap:12px;margin-top:4px}
.social span{width:33px;height:33px;border-radius:50%;border:2px solid #fff;display:block}
.foot-rule{left:0;top:3935px;width:1200px;border-top:1px solid rgba(255,255,255,.25)}
.foot-mark{left:578px;top:3925px;width:44px;height:44px;border-radius:50%;border:5px solid #fff}
.copyright{left:0;top:3993px;width:1200px;text-align:center;color:#e3f6f5;font-size:15px}
</style>
</head>
<body>
<div class="page">

  <!-- hero -->
  <div class="abs hero-photo" role="img" aria-label="Smiling woman in a straw hat petting a happy dog wearing sunglasses and a hat in a sunny park"></div>
  <div class="abs brand-dot"></div>
  <div class="abs brand display">Tumble Tail</div>
  <nav class="abs nav">
    <a class="home" href="#">Home</a>
    <a class="shop" href="#">Shop</a>
    <a class="story" href="#">Our Story</a>
    <a class="blog" href="#">Boop Blog</a>
    <a class="history" href="#">Pet History 101</a>
  </nav>
  <div class="abs nav-icons">
    <svg width="24" height="24" viewBox="0 0 24 24" fill="none" stroke="#fff" stroke-width="3"><circle cx="10" cy="10" r="7"/><path d="M15 15l6 6"/></svg>
    <svg width="30" height="26" viewBox="0 0 30 26" fill="none" stroke="#fff" stroke-width="2.5"><path d="M1 3h5l4 14h15l3-10H8"/><circle cx="12" cy="22" r="2"/><circle cx="23" cy="22" r="2"/></svg>
  </div>
  <div class="abs cart-count">0</div>

  <svg class="abs hero-blob" width="360" height="335" viewBox="0 0 360 335">
    <path d="M175 8 C260 0 350 30 356 120 C362 215 320 300 220 326 C130 348 30 318 10 230 C-8 150 20 70 70 35 C100 15 140 10 175 8Z" fill="var(--teal)"/>
  </svg>
  <div class="abs hero-title display">Tumble Tail Pet Supplies and Accessories</div>
  <div class="abs btn-shop display">Shop Now</div>
  <div class="abs arrow" style="left:64px;top:376px"></div>
  <div class="abs arrow" style="left:1095px;top:370px"></div>

  <!-- promo -->
  <svg class="abs promo" width="1200" height="560" viewBox="0 0 1200 560" role="img" aria-label="Golden retriever and tabby cat eating kibble from paw-print bowls on a grey backdrop">
    <defs>
      <linearGradient id="promoGrad" x1="0" y1="0" x2="1" y2="1">
        <stop offset="0" stop-color="#8e8d99"/>
        <stop offset=".35" stop-color="#c9b49b"/>
        <stop offset=".6" stop-color="#a3a2ae"/>
        <stop offset="1" stop-color="#7e7d89"/>
      </linearGradient>
    </defs>
    <path d="M0 20 C250 -10 500 10 720 40 C900 62 1060 55 1200 30 L1200 520 C1000 500 700 530 400 545 C220 552 90 540 0 520Z" fill="url(#promoGrad)"/>
  </svg>
  <svg class="abs" style="left:570px;top:780px" width="312" height="285" viewBox="0 0 312 285">
    <path d="M150 4 C235 0 300 50 308 130 C314 200 280 262 210 278 C140 294 40 280 12 210 C-10 150 10 70 60 35 C88 15 115 6 150 4Z" fill="var(--teal)"/>
  </svg>
  <div class="abs promo-title display">50% OFF Sale going on now! Because we love you too</div>

  <!-- furry favorites -->
  <div class="abs sec-mark" style="left:584px;top:1282px"></div>
  <h2 class="abs sec-title display" style="top:1318px">Furry Favorites</h2>

  <div class="abs card" style="left:121px;top:1424px">
    <div class="shot" role="img" aria-label="Tub of tropical fish flakes" style="background:linear-gradient(#2a2a2a,#f2d32b 45%,#3577c9)"></div>
    <div class="cart"><svg width="16" height="14" viewBox="0 0 30 26" fill="none" stroke="#fff" stroke-width="3"><path d="M1 3h5l4 14h15l3-10H8"/></svg></div>
    <div class="name">Nemo enim ipsam</div><div class="desc">voluptatem quia volupta</div><div class="rule"></div><div class="price">$25.00</div>
  </div>
  <div class="abs card" style="left:364px;top:1424px">
    <div class="shot" role="img" aria-label="Two bags of soft dog treats" style="background:linear-gradient(90deg,#d92d2d,#c9803d,#d92d2d)"></div>
    <div class="cart"><svg width="16" height="14" viewBox="0 0 30 26" fill="none" stroke="#fff" stroke-width="3"><path d="M1 3h5l4 14h15l3-10H8"/></svg></div>
    <div class="name">Nemo enim ipsam</div><div class="desc">voluptatem quia volupta</div><div class="rule"></div><div class="price">$25.00</div>
  </div>
  <div class="abs card" style="left:607px;top:1424px">
    <div class="shot" role="img" aria-label="Bag of dry dog food with wet food tins" style="background:linear-gradient(#2f9a5a,#f1f1f1 50%,#b49a74)"></div>
    <div class="cart"><svg width="16" height="14" viewBox="0 0 30 26" fill="none" stroke="#fff" stroke-width="3"><path d="M1 3h5l4 14h15l3-10H8"/></svg></div>
    <div class="name">Nemo enim ipsam</div><div class="desc">voluptatem quia volupta</div><div class="rule"></div><div class="price">$25.00</div>
  </div>
  <div class="abs card" style="left:850px;top:1424px">
    <div class="shot" role="img" aria-label="Black mesh pet carrier with toys and a collar" style="background:linear-gradient(#3a3a3a,#5a5a5a 55%,#e9e9e9 70%,#43b04a)"></div>
    <div class="cart"><svg width="16" height="14" viewBox="0 0 30 26" fill="none" stroke="#fff" stroke-width="3"><path d="M1 3h5l4 14h15l3-10H8"/></svg></div>
    <div class="name">Nemo enim ipsam</div><div class="desc">voluptatem quia volupta</div><div class="rule"></div><div class="price">$25.00</div>
  </div>

  <div class="abs card" style="left:121px;top:1824px">
    <div class="shot" role="img" aria-label="Stack of wet dog food trays" style="background:linear-gradient(#c9a46a,#e9dcc2 50%,#6a67b0)"></div>
    <div class="cart"><svg width="16" height="14" viewBox="0 0 30 26" fill="none" stroke="#fff" stroke-width="3"><path d="M1 3h5l4 14h15l3-10H8"/></svg></div>
    <div class="name">Nemo enim ipsam</div><div class="desc">voluptatem quia volupta</div><div class="rule"></div><div class="price">$25.00</div>
  </div>
  <div class="abs card" style="left:364px;top:1824px">
    <div class="shot" role="img" aria-label="Can of chicken cat food" style="background:linear-gradient(90deg,#a61f7e,#d84aa6,#a61f7e)"></div>
    <div class="cart"><svg width="16" height="14" viewBox="0 0 30 26" fill="none" stroke="#fff" stroke-width="3"><path d="M1 3h5l4 14h15l3-10H8"/></svg></div>
    <div class="name">Nemo enim ipsam</div><div class="desc">voluptatem quia volupta</div><div class="rule"></div><div class="price">$25.00</div>
  </div>
  <div class="abs card" style="left:607px;top:1824px">
    <div class="shot" role="img" aria-label="Red and black dog collar" style="background:linear-gradient(135deg,#fff 20%,#d82a2a 45%,#222 70%,#fff)"></div>
    <div class="cart"><svg width="16" height="14" viewBox="0 0 30 26" fill="none" stroke="#fff" stroke-width="3"><path d="M1 3h5l4 14h15l3-10H8"/></svg></div>
    <div class="name">Nemo enim ipsam</div><div class="desc">voluptatem quia volupta</div><div class="rule"></div><div class="price">$25.00</div>
  </div>
  <div class="abs card" style="left:850px;top:1824px">
    <div class="shot" role="img" aria-label="Bag of adult dry cat food" style="background:linear-gradient(#3f8c3a,#5aa24a 60%,#d9532b)"></div>
    <div class="cart"><svg width="16" height="14" viewBox="0 0 30 26" fill="none" stroke="#fff" stroke-width="3"><path d="M1 3h5l4 14h15l3-10H8"/></svg></div>
    <div class="name">Nemo enim ipsam</div><div class="desc">voluptatem quia volupta</div><div class="rule"></div><div class="price">$25.00</div>
  </div>

  <!-- pay later -->
  <svg class="abs paylater" width="1200" height="480" viewBox="0 0 1200 480" role="img" aria-label="Woman in sunglasses playing with her dog outdoors, tinted orange">
    <defs>
      <linearGradient id="payGrad" x1="0" y1="0" x2="1" y2="0">
        <stop offset="0" stop-color="#e27a4a"/>
        <stop offset=".5" stop-color="#eb9a6d"/>
        <stop offset="1" stop-color="#d9703f"/>
      </linearGradient>
    </defs>
    <path d="M0 40 C300 80 600 60 850 30 C1000 12 1120 5 1200 8 L1200 435 C1000 440 700 470 400 465 C220 462 90 450 0 440Z" fill="url(#payGrad)"/>
  </svg>
  <div class="abs sec-mark" style="left:584px;top:2392px;border-color:#fff"></div>
  <h2 class="abs pay-title display">Buy Now, Pay Later</h2>
  <div class="abs pay-btn" style="left:332px"><span style="display:inline-block;width:34px;height:34px;border-radius:50%;background:#4a45c4;margin-right:14px"></span>Crumbpay</div>
  <div class="abs pay-btn" style="left:611px">Tallyo</div>

  <!-- testimonials -->
  <div class="abs sec-mark" style="left:584px;top:2832px"></div>
  <h2 class="abs sec-title display" style="top:2873px">Testimonials</h2>

  <div class="abs quote" style="left:144px;top:2972px">
    <div class="avatar" role="img" aria-label="Black and tan dog carrying a ball in a field" style="background:radial-gradient(#5a4a3a,#a7b08a)"></div>
    <div class="who">Bella</div>
    <div class="words">“ Before Tumble Tail my human bought me gifts that made me want to dig a hole under the fence and run. Now I still dig, but it’s to bury all my awesome toys! ”</div>
  </div>
  <div class="abs quote" style="left:612px;top:2972px">
    <div class="avatar" role="img" aria-label="Tabby cat looking out of a window" style="background:radial-gradient(#b8aa96,#4a4038)"></div>
    <div class="who">Leo</div>
    <div class="words">My favorite thing to do is watch the birds out the window. Those birds are lucky my house is full of comfy stuff from Tumble Tail so I don’t ever want to leave.</div>
  </div>
  <div class="abs quote" style="left:144px;top:3245px">
    <div class="avatar" role="img" aria-label="Golden retriever portrait on grass" style="background:radial-gradient(#c98a3e,#4f6a2e)"></div>
    <div class="who">Max</div>
    <div class="words">Tumble Tail is the absolute best! Now if you’ll excuse me I think I heard someone drop some food on the floor.</div>
  </div>
  <div class="abs quote" style="left:612px;top:3245px">
    <div class="avatar" role="img" aria-label="Blue fish swimming in an aquarium" style="background:radial-gradient(#3f55d9,#0e1c5a)"></div>
    <div class="who">Dora</div>
    <div class="words">I could rave about Tumble Tail until I was blue in the gills! Those other brands just seem a bit fishy to me.</div>
  </div>

  <!-- footer -->
  <footer class="abs footer"></footer>
  <div class="abs rewards">
    <svg width="16" height="16" viewBox="0 0 16 16" fill="none" stroke="#fff" stroke-width="1.6"><rect x="2" y="6" width="12" height="8"/><path d="M1 6h14M8 6v8M8 6C6 2 3 3 5 6M8 6c2-4 5-3 3 0"/></svg>
    REWARDS
  </div>
  <div class="abs chat">
    <svg width="22" height="20" viewBox="0 0 22 20"><path d="M3 2h16a2 2 0 0 1 2 2v9a2 2 0 0 1-2 2H9l-5 4v-4H3a2 2 0 0 1-2-2V4a2 2 0 0 1 2-2z" fill="#fff"/><circle cx="7" cy="9" r="1.3" fill="#6f8ecf"/><circle cx="11" cy="9" r="1.3" fill="#6f8ecf"/><circle cx="15" cy="9" r="1.3" fill="#6f8ecf"/></svg>
  </div>
  <div class="abs foot-dot"></div>
  <div class="abs foot-brand display">Tumble Tail</div>

  <div class="abs foot-col" style="left:406px;top:3683px">
    <h4>COMPANY</h4>
    <ul><li>Shop</li><li>Our Story</li><li>Boop Blog</li><li>Pet History 1010</li></ul>
  </div>
  <div class="abs foot-col" style="left:614px;top:3683px">
    <h4>B.HELP &amp; SUPPORT</h4>
    <ul><li>Returns &amp; Exchanges</li><li>FAQ</li><li>hello@tumbletail.com</li><li>Search</li></ul>
  </div>
  <div class="abs foot-col" style="left:866px;top:3685px">
    <h4>CONTACT US</h4>
    <div class="contact-row">
      <svg width="18" height="18" viewBox="0 0 24 24" fill="#fff"><path d="M6.6 10.8a15.1 15.1 0 0 0 6.6 6.6l2.2-2.2c.3-.3.7-.4 1-.2 1.1.4 2.3.6 3.6.6.6 0 1 .4 1 1V20c0 .6-.4 1-1 1A17 17 0 0 1 3 4c0-.6.4-1 1-1h3.5c.6 0 1 .4 1 1 0 1.3.2 2.5.6 3.6.1.3 0 .7-.2 1z"/></svg>
      <div>Phone:<br>555 0140 2270</div>
    </div>
    <div class="contact-row">
      <svg width="18" height="14" viewBox="0 0 24 18" fill="#fff"><path d="M0 0h24v18H0z"/><path d="M0 0l12 9 12-9" stroke="#2bb1ae" stroke-width="2" fill="none"/></svg>
      <div>Email:<br>hello@tumbletail.com</div>
    </div>
    <div class="social"><span></span><span></span><span></span></div>
  </div>

  <div class="abs foot-rule"></div>
  <div class="abs foot-mark" style="background:var(--teal)"></div>
  <div class="abs copyright">Copyright 2021 tumbletail.com: All rights reserved</div>
</div>
</body>
</html>
```